Red Kettle Pictures BIz Card

This will be a biz card for our independent film company
RED KETTLE PICTURES

we have a logo and i need to figure out how to post it to you!

Here is the info we need on the card:

LOGO

dorinda pratchek (lower case!)
dP@RedKettlePix.example
512-684-2273

Red Kettle Pictures, LLC
www.RedKettlePix.example

stories that matter (tagline)

Target Market(s)

adults in the entertainment industry in USA.
need something creative feeling, a bit funky, not to overt.
something eye catchy that people will be inclined to keep.

ask me any questions you have!

Industry/Entity Type

It Company

Requirements
Must have
• good looking! clean and easy to get the contact info. not too busy.
Nice to have
• love the cards where the design is "continued" on the back side.

perhaps the tag and logo on the back side?!?

open to ideas!
Should not have
• nothing "cartoonish"

```html
<!DOCTYPE html>
<html lang="en">
<head>
<meta charset="utf-8">
<title>Red Kettle Pictures – Business Card</title>
<link href="https://fonts.googleapis.com/css2?family=Arimo:wght@400;700&family=Pinyon+Script&display=swap" rel="stylesheet">
<style>
  :root {
    --brand-red: #ec2d2c;
    --paper: #ffffff;
    --ink: #111111;
    --edge: #555555;
    --stage: #ffffff;
  }
  html, body {
    margin: 0;
    padding: 0;
    width: 1200px;
    height: 812px;
    overflow: hidden;
    background: var(--stage);
  }
  .sheet {
    position: relative;
    width: 1200px;
    height: 812px;
  }
  .card {
    position: absolute;
    left: 277px;
    width: 618px;
    height: 310px;
    box-sizing: border-box;
    border: 1px solid var(--edge);
    overflow: hidden;
    font-family: "Arimo", Arial, sans-serif;
  }
  .card--front { top: 45px; background: var(--paper); }
  .card--back { top: 447px; background: var(--brand-red); }
  .card__shapes {
    position: absolute;
    inset: 0;
    width: 100%;
    height: 100%;
  }
  .shape--red { fill: var(--brand-red); }
  .shape--white { fill: var(--paper); }

  .wordmark {
    position: absolute;
    left: 27px;
    top: 24px;
    margin: 0;
    font-size: 45px;
    font-weight: 400;
    letter-spacing: -0.5px;
    color: var(--ink);
    line-height: 1;
    white-space: nowrap;
  }
  .contact {
    position: absolute;
    left: 196px;
    top: 138px;
    margin: 0;
    color: var(--paper);
    font-size: 16px;
    line-height: 22px;
    font-style: normal;
  }
  .contact__group + .contact__group { margin-top: 21px; }
  .contact__line { display: block; }

  .tagline {
    position: absolute;
    left: 0;
    right: 0;
    top: 134px;
    margin: 0;
    text-align: center;
    font-family: "Pinyon Script", cursive;
    font-size: 31px;
    color: var(--paper);
    padding-left: 4px;
  }
</style>
</head>
<body>
<main class="sheet">
  <section class="card card--front" aria-label="Business card front">
    <svg class="card__shapes" viewBox="0 0 618 310" aria-hidden="true">
      <path class="shape--red" d="M172 310 C158 255 156 175 166 128 C172 105 192 98 226 100 C380 108 530 135 618 172 L618 310 Z"/>
      <circle class="shape--red" cx="14" cy="207" r="46"/>
    </svg>
    <h1 class="wordmark">Red Kettle Pictures</h1>
    <address class="contact">
      <div class="contact__group">
        <span class="contact__line">dorinda pratchek</span>
        <span class="contact__line">dP@RedKettlePix.example</span>
        <span class="contact__line">512-684-2273</span>
      </div>
      <div class="contact__group">
        <span class="contact__line">Red Kettle Pictures, LLC</span>
        <span class="contact__line">www.RedKettlePix.example</span>
      </div>
    </address>
  </section>

  <section class="card card--back" aria-label="Business card back">
    <svg class="card__shapes" viewBox="0 0 618 310" aria-hidden="true">
      <path class="shape--white" d="M0 172 C38 190 72 222 72 258 C72 282 58 298 40 310 L0 310 Z"/>
      <circle class="shape--white" cx="618" cy="208" r="43"/>
    </svg>
    <p class="tagline">stories that matter</p>
  </section>
</main>
</body>
</html>
```